Funky Cloud Security Startup wants a cutting edge website

We're looking for a clean and simple website to be able to sell out cutting edge Cloud Security products. We already have a logo and business codes to give you a view of the style/colours etc (see attached). Really looking for something similar to plumvane.com , tarvimo.com and if push comes to shove then our competitors vesta harbor.com.au don't have a bad site either.

We're still working through the content sections but want to have a home for the following types of content immediately:

Products (4 of them)
Company
Technology Partners
Press/News
Contact Us
Support
Login

and the site will need to expand to accommodate

Buy
Case Studies
Channel Partners

at some point in the future

On the bottom Nav we want:
* Privacy Policy
* Terms of Use
* Contact
* WorkWeave
* Chirpnest

The home page should an image rotator on it with some suitably cool images and call to actions as text hovering over them.

We need it to be easily editable in dreamweaver so a template is a must, it should also be completely CSS driven and adaptive so will work on mobile, tablet and desktop - you know the score.

We're hosting on a linux server so PHP code for any crazy stuff is a must.

Really exciting project as this will be a huge company with major investors backing it internationally so you will be able to put your name against the next Glimmerly/Chirpnest/Coinrove.

Go crazy with your creativity, just remember vorlu's slogan is "Security made simple"

We look forward to seeing your creations, good luck!

```html
<!DOCTYPE html>
<html lang="en">
<head>
<meta charset="utf-8">
<title>vorlu — security made simple</title>
<link rel="stylesheet" href="https://fonts.googleapis.com/css2?family=Ubuntu:wght@300;400&family=Arimo:wght@400;700&display=swap">
<style>
  :root {
    --blue: #2496c9;
    --blue-dark: #1877a6;
    --blue-light: #3eaee0;
    --green: #b3d334;
    --green-btn: #8dc21f;
    --ink: #333333;
    --grey-text: #555555;
    --band-grey: #ececec;
    --rule: #cfcfcf;
    --footer: #505050;
    --footer-text: #e2e2e2;
    --submit: #5e5e5e;
    --white: #ffffff;
    --black: #050505;
  }
  * { margin: 0; padding: 0; box-sizing: border-box; }
  html, body { width: 1200px; height: 2375px; overflow: hidden; background: var(--white); }
  body { position: relative; font-family: "Arimo", Arial, sans-serif; color: var(--ink); }
  .abs { position: absolute; }
  .light { font-family: "Ubuntu", "Helvetica Neue", sans-serif; font-weight: 300; }

  /* header */
  .site-header { left: 0; top: 0; width: 1200px; height: 105px; background: var(--white); }
  .brand { left: 131px; top: 28px; display: flex; align-items: center; gap: 12px; }
  .brand-dot { width: 46px; height: 46px; border-radius: 50%; background: var(--blue); }
  .brand-name { font-family: "Ubuntu", sans-serif; font-weight: 400; font-size: 56px; color: #5a5a5a; line-height: 1; letter-spacing: -1px; }
  .tagline { right: 138px; top: 42px; font-size: 34px; color: #555; }

  .main-nav { left: 0; top: 105px; width: 1200px; height: 42px;
    background: linear-gradient(#3aa8d8, var(--blue) 55%, #1a80b2); border-top: 2px solid #7cc7ea; }
  .main-nav ul { list-style: none; display: flex; position: absolute; left: 134px; top: 9px; }
  .main-nav li { font-size: 15.5px; color: var(--white); margin-right: 31px; font-family: "Ubuntu", sans-serif; white-space: nowrap; }

  /* hero */
  .hero { left: 0; top: 147px; width: 1200px; height: 391px; overflow: hidden; }
  .hero-photo { position: absolute; inset: 0;
    background: linear-gradient(90deg, #5d5852 0%, #8a8780 18%, #d9dde0 30%, #b7bec5 40%, #2f4660 62%, #1a2c44 80%, #6c8aa8 100%); }
  .hero-panel { position: absolute; left: 560px; top: 0; width: 540px; height: 391px; background: var(--black);
    clip-path: polygon(30px 0, 540px 0, 510px 391px, 0 391px); }
  .hero-copy { left: 570px; top: 30px; width: 490px; text-align: center; font-size: 33px; line-height: 37px; color: var(--white); white-space: nowrap; }
  .btn { display: flex; align-items: center; gap: 8px; height: 35px; padding: 0 12px; color: var(--white); font-size: 24px; line-height: 35px; white-space: nowrap; }
  .btn svg { width: 20px; height: 20px; flex: none; }
  .btn-green { background: var(--green-btn); }
  .btn-blue { background: var(--blue); }
  .hero .btn { left: 583px; top: 239px; width: 157px; }
  .slider-dots { left: 887px; top: 364px; display: flex; gap: 4px; }
  .slider-dots span { width: 13px; height: 13px; background: var(--blue); }
  .slider-dots span:first-child { background: var(--green); }

  /* products */
  .product { top: 594px; width: 220px; }
  .product-art { width: 130px; height: 130px; border-radius: 22px; margin-left: 20px;
    background: radial-gradient(circle at 50% 40%, #6cc6f2, #1b78b6 70%, #1c2f45); }
  .product-title { margin-top: 30px; font-size: 22px; color: var(--blue); text-align: center; width: 170px; white-space: nowrap; }
  .product-text { margin-top: 8px; font-size: 12.6px; line-height: 15px; color: var(--grey-text); width: 210px; }

  /* about */
  .about { left: 0; top: 891px; width: 1200px; height: 413px; background: var(--black); overflow: hidden; }
  .about-photo { position: absolute; left: 150px; top: 0; width: 560px; height: 413px;
    background: radial-gradient(ellipse at 45% 50%, #5a6168 0%, #2a2e33 45%, #0b0c0e 75%, #050505 100%); }
  .about-title { left: 612px; top: 45px; font-size: 68px; color: var(--white); white-space: nowrap; }
  .about-copy { left: 612px; top: 140px; font-size: 18px; line-height: 28.5px; color: var(--white); font-family: "Ubuntu", sans-serif; font-weight: 300; white-space: nowrap; }
  .about .btn { left: 612px; top: 312px; width: 156px; }

  /* partners */
  .partners { left: 0; top: 1304px; width: 1200px; height: 118px; background: var(--band-grey); }
  .partners .rule { position: absolute; left: 160px; width: 876px; height: 1px; background: var(--rule); }
  .partner-strip { left: 162px; top: 49px; display: flex; gap: 22px; align-items: center; }
  .partner-badge { height: 20px; background: #6a6a6a; border-radius: 2px; }

  /* news */
  .news-title { left: 0; width: 1200px; top: 1466px; text-align: center; font-size: 22px; color: #444; }
  .news-item { top: 1529px; width: 230px; }
  .date-box { position: absolute; left: 0; top: 0; width: 73px; height: 79px; background: var(--blue); color: var(--white); text-align: center; }
  .date-box::after { content: ""; position: absolute; right: -10px; top: 16px; border-left: 10px solid var(--blue); border-top: 9px solid transparent; border-bottom: 9px solid transparent; }
  .date-day { font-size: 38px; line-height: 1; padding-top: 10px; font-family: "Ubuntu", sans-serif; }
  .date-month { font-size: 15px; margin-top: 6px; }
  .news-body { position: absolute; left: 95px; top: 0; width: 125px; }
  .news-head { font-size: 11.5px; font-weight: 700; line-height: 13px; color: #222; }
  .news-text { margin-top: 5px; font-size: 11.5px; line-height: 13.5px; color: var(--grey-text); }

  /* contact */
  .contact { left: 0; top: 1729px; width: 1200px; height: 424px; background: var(--green); color: var(--white); }
  .contact-title { left: 0; width: 1200px; top: 48px; text-align: center; font-size: 46px; }
  .contact-lede { left: 0; width: 1200px; top: 107px; text-align: center; font-size: 20.5px; line-height: 25px; font-family: "Ubuntu", sans-serif; font-weight: 300; }
  .field { background: var(--white); color: #444; font-size: 15px; padding: 14px 16px; }
  .submit { background: var(--submit); display: flex; align-items: center; justify-content: center; }

  /* footer */
  .site-footer { left: 0; top: 2153px; width: 1200px; height: 222px; background: var(--footer); color: var(--footer-text); }
  .footer-heading { font-size: 22px; color: var(--white); white-space: nowrap; }
  .footer-links { list-style: none; font-size: 12.5px; line-height: 17.5px; white-space: nowrap; }
  .social { display: flex; gap: 16px; }
  .social span { width: 42px; height: 42px; border-radius: 50%; background: #9a9a9a; }
  .footer-small { font-size: 12px; line-height: 15px; white-space: nowrap; }
  .footer-phone { display: flex; align-items: center; gap: 6px; font-size: 24px; font-family: "Ubuntu", sans-serif; font-weight: 300; white-space: nowrap; }
  .footer-brand { left: 858px; top: 43px; display: flex; align-items: center; gap: 10px; }
  .footer-brand .brand-dot { width: 40px; height: 40px; background: #e6e6e6; }
  .footer-brand .brand-name { color: #e6e6e6; font-size: 50px; }
</style>
</head>
<body>

<header class="site-header abs">
  <div class="brand abs"><span class="brand-dot"></span><span class="brand-name">vorlu.</span></div>
  <div class="tagline abs light">security made simple</div>
</header>

<nav class="main-nav abs">
  <ul>
    <li>company</li><li>technology partners</li><li>press/news</li><li>contact us</li>
    <li>support</li><li>buy</li><li>case studies</li><li>channel partners</li><li>login</li>
  </ul>
</nav>

<section class="hero abs">
  <div class="hero-photo" role="img" aria-label="Business person using a tablet in front of server racks and a cloud"></div>
  <div class="hero-panel"></div>
  <p class="hero-copy abs light">Lorem ipsum dolor sit amet,<br>consectetur adipisicing elit,<br>sed do eiusmod tempor<br>incididunt ut labore et dolore<br>magna aliqua.</p>
  <a class="btn btn-green abs light">
    <svg viewBox="0 0 20 20"><circle cx="10" cy="10" r="9" fill="#fff"/><path d="M5 10h8M10 6l4 4-4 4" stroke="#8dc21f" stroke-width="2.4" fill="none"/></svg>more info
  </a>
  <div class="slider-dots abs"><span></span><span></span><span></span><span></span></div>
</section>

<section class="products">
  <div class="product abs" style="left:132px">
    <div class="product-art" role="img" aria-label="Glossy blue game controller icon"></div>
    <h3 class="product-title light">secured gaming</h3>
    <p class="product-text">Duis aute irure dolor in reprehderit in voluptate velit esse cillum dolore eu fugiat nulla pariatur.</p>
  </div>
  <div class="product abs" style="left:378px">
    <div class="product-art" role="img" aria-label="Blue cloud with upload arrow icon"></div>
    <h3 class="product-title light">safe cloud media</h3>
    <p class="product-text">Excepteur sint occaecat cupidatat non proident, sunt in cua qui officia deserunt mollit anim idborum.</p>
  </div>
  <div class="product abs" style="left:613px">
    <div class="product-art" role="img" aria-label="Phone with sync arrows icon"></div>
    <h3 class="product-title light">secured mobile</h3>
    <p class="product-text">Sed ut perspiciatis, unde omnis iste natus error sit voluptatem accusantium doloremque laud.</p>
  </div>
  <div class="product abs" style="left:867px">
    <div class="product-art" role="img" aria-label="Server stack with cloud icon" style="background:radial-gradient(circle at 50% 35%,#f0f0f0,#9aa0a6 55%,#2a2d31)"></div>
    <h3 class="product-title light">cloud hosting</h3>
    <p class="product-text">Nemo enim ipsam voluptatem, quia voluptas sit, aspernatur aut odit aut fugit, sed quia.</p>
  </div>
</section>

<section class="about abs">
  <div class="about-photo" role="img" aria-label="Person in a suit holding a glass tablet showing a cloud network sketch"></div>
  <h2 class="about-title abs light">who is vorlu?</h2>
  <p class="about-copy abs">At vero eos et accusamus et iusto odio dignissimos<br>ducimus, qui blanditiis praesentium voluptatum<br>deleniti atque corrupti, quos dolores et quas<br>molestias excepturi sint, obcaecati cupiditate non<br>provident, similique sunt in culpa.</p>
  <a class="btn btn-blue abs light">
    <svg viewBox="0 0 20 20"><circle cx="10" cy="10" r="9" fill="#fff"/><path d="M5 10h8M10 6l4 4-4 4" stroke="#2496c9" stroke-width="2.4" fill="none"/></svg>more info
  </a>
</section>

<section class="partners abs" aria-label="Partners">
  <span class="rule" style="top:29px"></span>
  <span class="rule" style="top:89px"></span>
  <div class="partner-strip abs">
    <span class="partner-badge" style="width:84px"></span>
    <span class="partner-badge" style="width:108px"></span>
    <span class="partner-badge" style="width:124px"></span>
    <span class="partner-badge" style="width:114px"></span>
    <span class="partner-badge" style="width:108px"></span>
    <span class="partner-badge" style="width:80px"></span>
    <span class="partner-badge" style="width:108px"></span>
  </div>
</section>

<h2 class="news-title abs light">press / news</h2>
<article class="news-item abs" style="left:144px">
  <div class="date-box"><div class="date-day">12</div><div class="date-month">NOV</div></div>
  <div class="news-body"><h4 class="news-head">LOREM IPSUM DOLOR AMET</h4><p class="news-text">Psum dolor sit amet, consectetuer adipiscing elit, sed diam nonummy nibh euismod.</p></div>
</article>
<article class="news-item abs" style="left:380px">
  <div class="date-box"><div class="date-day">04</div><div class="date-month">NOV</div></div>
  <div class="news-body"><h4 class="news-head">EXCEPTEUR SINT OCCAECAT CUPID</h4><p class="news-text">Duis aute irure dolor in reprehderit in voluptate velit esse cillum dolore eu fugiat nulla pariatur.</p></div>
</article>
<article class="news-item abs" style="left:614px">
  <div class="date-box"><div class="date-day">27</div><div class="date-month">OCT</div></div>
  <div class="news-body"><h4 class="news-head">NEMO ENIM IPSAM VOLUPTATEM</h4><p class="news-text">Excepteur sint occa ecat cupidatat non proident, sunt in cua qui officia deserunt mollit anim idborum.</p></div>
</article>
<article class="news-item abs" style="left:849px">
  <div class="date-box"><div class="date-day">15</div><div class="date-month">OCT</div></div>
  <div class="news-body"><h4 class="news-head">DUIS AUTE IRURE DOLOR IN REPRE</h4><p class="news-text">Nemo enim ipsam voluptatem, quia voluptas sit, aspernatur aut odit aut fugit, sed quia.</p></div>
</article>

<section class="contact abs">
  <h2 class="contact-title abs light">contact us</h2>
  <p class="contact-lede abs">We'd really love to hear from you so why not give us a call on 1230 555 018 or<br>drop us an email and we'll get back to you as soon as we can.</p>
  <div class="field abs" style="left:192px;top:185px;width:394px;height:46px">Full Name</div>
  <div class="field abs" style="left:192px;top:243px;width:394px;height:46px">Email Address</div>
  <div class="field abs" style="left:192px;top:304px;width:394px;height:44px">Phone Number</div>
  <div class="field abs" style="left:614px;top:185px;width:394px;height:104px">Message</div>
  <div class="submit abs" style="left:614px;top:304px;width:394px;height:44px">
    <svg width="34" height="24" viewBox="0 0 34 24"><rect x="1" y="1" width="32" height="22" fill="#fff"/><path d="M1 1l16 13L33 1M1 23l12-11M33 23L21 12" stroke="#5e5e5e" stroke-width="1.6" fill="none"/></svg>
  </div>
</section>

<footer class="site-footer abs">
  <h3 class="footer-heading abs light" style="left:139px;top:36px">NAVIGATION</h3>
  <ul class="footer-links abs" style="left:142px;top:78px">
    <li>Home</li><li>Company</li><li>Technology Partners</li><li>Press/News</li><li>Contact Us</li><li>Support</li>
  </ul>
  <ul class="footer-links abs" style="left:284px;top:78px">
    <li>Buy</li><li>Case Studies</li><li>Channel Partners</li><li>Login</li><li>Privacy Policy</li><li>Terms of Use</li>
  </ul>
  <h3 class="footer-heading abs light" style="left:420px;top:36px">CONNECT</h3>
  <div class="social abs" style="left:420px;top:82px">
    <span role="img" aria-label="Glimmerly"></span><span role="img" aria-label="Chirpnest"></span><span role="img" aria-label="WorkWeave"></span>
  </div>
  <h3 class="footer-heading abs light" style="left:633px;top:36px">CONTACT US</h3>
  <p class="footer-small abs" style="left:633px;top:76px">#38 street city, state, Country<br>email : info@harrowgate.com.au</p>
  <div class="footer-phone abs" style="left:630px;top:112px">
    <svg width="26" height="26" viewBox="0 0 26 26"><circle cx="13" cy="13" r="11.5" fill="none" stroke="#e2e2e2" stroke-width="2"/><path d="M9 7c1 0 1.5 2.5 1.5 3s-1 1-1 1.5c.5 2 2.5 4 4.5 4.5.5 0 1-1 1.5-1s3 .5 3 1.5-1.5 2.5-3 2.5C11 19 7 15 7 9.5 7 8 8 7 9 7z" fill="#e2e2e2"/></svg>012.555.0187
  </div>
  <div class="footer-brand abs"><span class="brand-dot"></span><span class="brand-name">vorlu.</span></div>
  <p class="footer-small abs" style="left:862px;top:115px">© Copyright vorlu. 2013.<br>All Rights Reserved</p>
</footer>

</body>
</html>
```